Label for a new Bourbon bottle

Name of the new Bourbon is Bolado. This will be a Straight Bourbon Finished in Sherry Casks. We are calling in Bolado to give it the look and feel of Spanish and Portuguese influence where sherry comes from. I've included some samples of labels in the US, you can also take a look at Spanish sherry bottle labels included too and get some inspiration, it can have traditional influence but with it's own style, not too focused on barrels. The proof will be 90, alc. by vol. 45%. Volume 750 ML.

Target Market(s)

Whiskey and Bourbon drinkers

Requirements
Must have
• Elegant, classy but not a mirror of what so many traditional labels look like, must feel high-end, expensive

```html
<!DOCTYPE html>
<html lang="en">
<head>
<meta charset="utf-8">
<title>Bolado Straight Bourbon Whiskey – Label</title>
<link href="https://fonts.googleapis.com/css2?family=Rye&family=Oswald:wght@700&family=Cinzel:wght@400;500&family=Pinyon+Script&display=swap" rel="stylesheet">
<style>
  :root {
    --paper: #fbfbfa;
    --brand-red: #8f2412;
    --band-red: #9a2a17;
    --gold: #c9a84a;
    --ink: #141414;
    --engraving: #c9c9c5;
    --photo-dark: #6a6a67;
    --photo-mid: #a9a9a6;
    --photo-light: #d9d9d6;
  }
  html, body {
    margin: 0;
    padding: 0;
    width: 1200px;
    height: 2880px;
    overflow: hidden;
    background: var(--paper);
  }
  .filters { position: absolute; width: 0; height: 0; }
  .label {
    position: relative;
    width: 1200px;
    height: 2880px;
    background: radial-gradient(ellipse at 50% 40%, #ffffff 0%, var(--paper) 70%, #f1f1ef 100%);
    overflow: hidden;
  }
  .established {
    position: absolute;
    top: 184px;
    font-family: "Pinyon Script", cursive;
    font-size: 74px;
    color: var(--gold);
    line-height: 1;
  }
  .established--word { left: 244px; }
  .established--year { left: 826px; }
  .farm-engraving {
    position: absolute;
    left: 402px;
    top: 110px;
    width: 369px;
    height: 236px;
    border-radius: 40px;
    background: radial-gradient(ellipse at 50% 55%, var(--engraving) 0%, #e2e2df 55%, rgba(251,251,250,0) 78%);
  }
  .brand-name {
    position: absolute;
    left: 0;
    top: 372px;
    width: 1200px;
    margin: 0;
    text-align: center;
    font-family: "Rye", serif;
    font-weight: 400;
    font-size: 176px;
    letter-spacing: 6px;
    line-height: 1;
    color: var(--brand-red);
    transform: scaleY(1.55);
    transform-origin: top center;
    filter: url(#distress);
  }
  .spirit-type {
    position: absolute;
    left: 0;
    top: 710px;
    width: 1200px;
    margin: 0;
    text-align: center;
    font-family: "Cinzel", serif;
    font-weight: 500;
    font-size: 60px;
    letter-spacing: 6px;
    line-height: 64px;
    color: var(--ink);
  }
  .hero-artwork {
    position: absolute;
    left: 34px;
    top: 900px;
    width: 1166px;
    height: 1200px;
    border-radius: 220px 0 200px 260px;
    background:
      radial-gradient(ellipse 30% 40% at 50% 30%, rgba(143,36,18,0.55) 0%, rgba(143,36,18,0) 100%),
      linear-gradient(135deg, var(--photo-light) 0%, var(--photo-mid) 45%, var(--photo-dark) 100%);
    opacity: 0.75;
  }
  .finish-note {
    position: absolute;
    left: 0;
    top: 2208px;
    width: 1200px;
    text-align: center;
    font-family: "Cinzel", serif;
    font-size: 54px;
    letter-spacing: 8px;
    color: var(--brand-red);
    line-height: 1;
  }
  .cask-type {
    position: absolute;
    left: 0;
    top: 2292px;
    width: 1200px;
    text-align: center;
    font-family: "Pinyon Script", cursive;
    font-size: 150px;
    color: var(--brand-red);
    line-height: 1;
  }
  .origin {
    position: absolute;
    left: 0;
    top: 2478px;
    width: 1200px;
    text-align: center;
    font-family: "Cinzel", serif;
    font-size: 53px;
    letter-spacing: 1px;
    color: var(--ink);
    line-height: 1;
  }
  .spec-band {
    position: absolute;
    left: 0;
    top: 2588px;
    width: 1200px;
    height: 292px;
    border-top: 9px solid var(--gold);
    box-sizing: border-box;
    background: linear-gradient(180deg, var(--band-red) 0%, #8c2413 100%);
  }
  .spec-band__mark {
    position: absolute;
    left: 94px;
    top: 96px;
    width: 86px;
    height: 86px;
    background: var(--gold);
  }
  .spec {
    position: absolute;
    top: 72px;
    width: 260px;
    text-align: center;
    color: var(--ink);
    font-family: "Oswald", sans-serif;
    font-weight: 700;
  }
  .spec__value {
    display: block;
    font-size: 84px;
    letter-spacing: 14px;
    line-height: 1;
    margin-right: -14px;
  }
  .spec__unit {
    display: block;
    margin-top: 14px;
    font-size: 40px;
    letter-spacing: 10px;
    line-height: 1;
    margin-right: -10px;
  }
  .spec--proof { left: 247px; }
  .spec--abv { left: 577px; }
  .spec--volume { left: 904px; }
  .spec-divider {
    position: absolute;
    top: 78px;
    width: 8px;
    height: 136px;
    border-radius: 4px;
    background: var(--gold);
  }
  .spec-divider--first { left: 517px; }
  .spec-divider--second { left: 877px; }
</style>
</head>
<body>
  <svg class="filters" aria-hidden="true" focusable="false">
    <filter id="distress" x="0" y="0" width="100%" height="100%">
      <feTurbulence type="fractalNoise" baseFrequency="0.7" numOctaves="2" seed="4" result="noise"/>
      <feColorMatrix in="noise" type="matrix" values="0 0 0 0 0  0 0 0 0 0  0 0 0 0 0  -9 0 0 0 5.2" result="speckle"/>
      <feComposite in="SourceGraphic" in2="speckle" operator="in" result="worn"/>
      <feDisplacementMap in="worn" in2="noise" scale="3" xChannelSelector="R" yChannelSelector="G"/>
    </filter>
  </svg>
  <main class="label">
    <span class="established established--word">Estd</span>
    <div class="farm-engraving" role="img" aria-label="Engraved farm scene with windmill, barn, silo, tree and ploughed fields"></div>
    <span class="established established--year">2021</span>

    <h1 class="brand-name">BOLADO</h1>
    <p class="spirit-type">STRAIGHT BOURBON<br>WHISKEY</p>

    <div class="hero-artwork" role="img" aria-label="Black and white photograph of a matador sweeping his cape before a charging bull, set over a large distressed red letter"></div>

    <div class="finish-note">FINISHED IN</div>
    <div class="cask-type">Sherry Casks</div>
    <div class="origin">PRODUCT OF SPAIN</div>

    <section class="spec-band">
      <span class="spec-band__mark"></span>
      <div class="spec spec--proof">
        <span class="spec__value">90</span>
        <span class="spec__unit">PROOF</span>
      </div>
      <span class="spec-divider spec-divider--first"></span>
      <div class="spec spec--abv">
        <span class="spec__value">45%</span>
        <span class="spec__unit">ALC/VOL</span>
      </div>
      <span class="spec-divider spec-divider--second"></span>
      <div class="spec spec--volume">
        <span class="spec__value">750</span>
        <span class="spec__unit">ML</span>
      </div>
    </section>
  </main>
</body>
</html>
```